Tembo & Lusani Advocates website

An interactive professional law firm website fully synchronized with social media pages.

Target Market(s)

Corporations and professionals

Industry/Entity Type

Professional Service

Number of Pages Required

5+ page

Font styles to use
Sans Serif

Colors

Designer to choose colors to be used in the design.

```html
<!DOCTYPE html>
<html lang="en">
<head>
<meta charset="utf-8">
<title>Tembo &amp; Lusani Advocates</title>
<link href="https://fonts.googleapis.com/css2?family=Encode+Sans:wght@300;400;600;700&family=Open+Sans:wght@400;600;700&display=swap" rel="stylesheet">
<style>
:root{
  --red:#8c1f24;
  --red-dark:#6e151a;
  --ink:#222;
  --muted:#555;
  --dark:#1c1a19;
  --light:#f1f1f1;
  --white:#fff;
}
*{box-sizing:border-box;margin:0;padding:0}
html,body{width:1200px;height:4651px;overflow:hidden}
body{font-family:"Open Sans",sans-serif;color:var(--ink);background:var(--white);position:relative}
.h{font-family:"Encode Sans",sans-serif}
section,header,footer{position:absolute;left:0;width:1200px}
.abs{position:absolute}
.label{font-size:13px;letter-spacing:2px;color:var(--red);font-weight:700;text-transform:uppercase}
.title{font-family:"Encode Sans",sans-serif;font-weight:300;font-size:38px;line-height:46px}
.photo{position:absolute}

/* header */
.topbar{top:0;height:118px}
.contact{left:95px;font-size:14px;display:flex;align-items:center;gap:10px}
.brand{left:440px;top:14px;width:330px;display:flex;align-items:center;gap:14px}
.mark{width:92px;height:64px;background:var(--red);color:#fff;display:flex;align-items:center;justify-content:center;font-family:"Encode Sans",sans-serif;font-weight:700;font-size:30px}
.brand-name{font-family:"Encode Sans",sans-serif;font-size:26px;line-height:29px;color:var(--ink)}
.brand-tag{position:absolute;left:440px;top:86px;width:330px;text-align:center;font-size:9px;letter-spacing:2px;color:var(--red);border-top:1px solid var(--red);padding-top:6px}
.btn-appt{left:960px;top:35px;width:146px;height:42px;background:var(--red);color:#fff;font-size:14px;display:flex;align-items:center;justify-content:center}

/* hero */
.hero{top:118px;height:682px}
.hero .photo{inset:0;background:linear-gradient(120deg,#2a1a10 0%,#6b4024 35%,#b57a3f 60%,#3b2414 100%)}
.nav{position:absolute;top:0;left:0;width:1200px;height:60px;background:rgba(20,16,14,.75);display:flex;justify-content:center;gap:42px;align-items:center}
.nav a{color:#fff;font-size:13px;font-weight:600;letter-spacing:1px;text-decoration:none}
.hero-title{left:95px;top:295px;color:#fff;font-family:"Encode Sans",sans-serif;font-weight:600;font-size:38px;letter-spacing:4px}
.hero-sub{left:95px;top:350px;background:var(--red);color:#fff;font-size:17px;padding:6px 14px}
.arrows{right:95px;top:640px;display:flex;gap:6px}
.arrows span{width:32px;height:32px;background:var(--red);display:flex;align-items:center;justify-content:center}

/* welcome */
.welcome{top:800px;height:331px;text-align:center}
.welcome .title{margin-top:30px}
.welcome p{width:900px;margin:16px auto 0;font-size:14.5px;line-height:24px;color:var(--muted)}
.more{font-size:12px;font-weight:700;letter-spacing:1px;color:var(--ink);border-bottom:2px solid var(--red);padding-bottom:3px;display:inline-block}
.welcome .more{margin-top:18px}

/* about */
.about{top:1131px;height:1079px}
.about .grey{left:0;top:651px;width:1200px;height:428px;background:var(--light)}
.about .statue{left:590px;top:40px;width:520px;height:610px;background:radial-gradient(ellipse at 55% 45%,#6d6a66 0%,#a8a6a3 45%,#fff 75%)}
.about .team{left:95px;top:450px;width:575px;height:380px;background:linear-gradient(180deg,#4a2b1e,#2a2421 60%,#1a1716)}
.about .copy{left:95px;top:40px;width:500px}
.about .copy p{margin-top:24px;font-size:14.5px;line-height:25px;color:var(--muted)}
.exp{left:670px;top:651px;width:435px;height:428px;background:var(--red);color:#fff;text-align:center;padding-top:70px}
.exp .small-mark{font-family:"Encode Sans",sans-serif;font-size:34px;font-weight:700}
.exp .big{font-family:"Encode Sans",sans-serif;font-weight:700;font-size:48px;letter-spacing:2px;margin-top:18px}
.exp .sub{font-family:"Encode Sans",sans-serif;font-weight:600;font-size:19px;letter-spacing:5px}
.exp .line{width:320px;height:1px;background:rgba(255,255,255,.6);margin:4px auto 0}
.exp p{font-size:14px;margin-top:26px}
.exp .btn{display:inline-block;margin-top:26px;border:2px solid #fff;padding:9px 20px;font-size:12px;letter-spacing:1px;font-weight:700}
.vm{left:95px;top:870px;width:520px}
.vm h4{font-size:13px;letter-spacing:2px;color:var(--red);margin-top:16px}
.vm p{font-size:14px;line-height:22px;color:var(--muted);margin-top:4px}

/* practice */
.practice{top:2210px;height:658px;background:linear-gradient(90deg,#141211 0%,#241e1a 60%,#3a2d24 100%)}
.practice .label{position:absolute;left:95px;top:80px}
.practice .title{position:absolute;left:95px;top:104px;color:#fff}
.card{position:absolute;top:250px;width:320px;height:340px;background:#fff;text-align:center;padding:0 28px}
.card .icon{width:104px;height:104px;border-radius:50%;background:var(--red);border:5px solid #fff;margin:-52px auto 0;display:flex;align-items:center;justify-content:center}
.card h3{font-size:14px;letter-spacing:2px;font-weight:700;margin-top:20px}
.card p{font-size:13.5px;line-height:21px;color:var(--muted);margin-top:12px}
.card .more{margin-top:16px}

/* stats */
.stats{top:2868px;height:356px;display:flex;justify-content:center;padding:0 60px}
.stat{width:270px;text-align:center;padding-top:50px;border-right:1px solid #ddd;margin-top:40px;height:260px}
.stat:last-child{border-right:none}
.stat .num{font-family:"Encode Sans",sans-serif;font-weight:700;font-size:40px;margin-top:14px}
.stat .lbl{font-size:12px;letter-spacing:2px;color:var(--red);font-weight:700;margin-top:6px;line-height:20px}

/* team */
.team-band{top:3224px;height:403px;background:var(--red)}
.member{position:absolute;top:80px;width:225px;height:260px;background:#fff;text-align:center}
.member .photo{left:25px;top:20px;width:175px;height:165px;background:linear-gradient(180deg,#c8c4be,#6b6259)}
.member h4{position:absolute;top:198px;width:100%;font-size:13px;letter-spacing:2px}
.member p{position:absolute;top:222px;width:100%;font-size:14px;color:var(--muted)}
.team-nav{position:absolute;top:160px;width:22px;height:22px;background:#1b1b1b;display:flex;align-items:center;justify-content:center}
.team-copy{position:absolute;left:890px;top:60px;color:#fff}
.team-copy .label{color:#fff}
.team-copy .title{font-size:30px;line-height:36px;margin-top:14px;color:#f2d4d4}
.team-copy .more{color:#fff;border-color:#fff;margin-top:14px}

/* clients */
.clients{top:3627px;height:350px}
.clients .label{position:absolute;left:95px;top:60px}
.clients .title{position:absolute;left:95px;top:84px;font-size:26px;line-height:32px}
.client{position:absolute;top:190px;height:90px;display:flex;align-items:center;gap:12px;font-family:"Open Sans",sans-serif;font-weight:700;font-size:24px;color:var(--ink)}
.client i{width:22px;height:22px;background:var(--red);display:block}
.c-arrows{position:absolute;right:95px;top:40px;display:flex;gap:6px}
.c-arrows span{width:24px;height:24px;background:var(--red);display:flex;align-items:center;justify-content:center}

/* quote */
.quote{top:3977px;height:441px}
.quote .photo{left:615px;top:0;width:585px;height:441px;background:linear-gradient(135deg,#f4f2ef,#b7b0a6 55%,#3c2c22)}
.quote .form{position:absolute;left:95px;top:40px;width:490px}
.quote h2{font-family:"Encode Sans",sans-serif;font-weight:400;font-size:26px;margin-top:8px}
.quote p{font-size:14px;line-height:22px;color:var(--muted);margin-top:8px}
.field{background:#ececec;height:40px;font-size:13px;color:#666;padding:12px;margin-top:10px}
.row{display:flex;gap:12px}
.row .field{flex:1}
.field.msg{height:80px}
.submit{display:inline-block;background:#151515;color:#fff;font-size:13px;padding:9px 28px;margin-top:14px}

/* footer */
.footer{top:4418px;height:170px;background:var(--red);color:#fff}
.footer h5{font-size:12.5px;letter-spacing:2px;font-weight:700}
.footer .addr{position:absolute;left:95px;top:30px;font-size:13px;line-height:20px}
.footer .addr p{margin-top:8px}
.footer .fmark{position:absolute;left:555px;top:40px;width:90px;text-align:center;font-family:"Encode Sans",sans-serif;font-weight:700;font-size:30px}
.footer .social{position:absolute;left:555px;top:92px;width:90px;display:flex;justify-content:center;gap:14px}
.footer .links{position:absolute;left:785px;top:30px;font-size:12.5px;letter-spacing:1px}
.footer .cols{display:flex;gap:70px;margin-top:10px;line-height:20px}
.copy-bar{top:4588px;height:63px;text-align:center;font-size:12px;color:#444;line-height:63px}
</style>
</head>
<body>

<header class="topbar">
  <div class="contact abs" style="top:28px">
    <svg width="16" height="12" viewBox="0 0 16 12"><rect x=".5" y=".5" width="15" height="11" fill="none" stroke="#222"/><path d="M1 1l7 6 7-6" fill="none" stroke="#222"/></svg>
    info@tembolusani.com
  </div>
  <div class="contact abs" style="top:62px">
    <svg width="16" height="16" viewBox="0 0 24 24"><path d="M6.6 10.8a15 15 0 006.6 6.6l2.2-2.2a1 1 0 011-.25 11.4 11.4 0 003.6.6 1 1 0 011 1V20a1 1 0 01-1 1A17 17 0 013 4a1 1 0 011-1h3.5a1 1 0 011 1 11.4 11.4 0 00.6 3.6 1 1 0 01-.25 1z" fill="#222"/></svg>
    0400 555 018
  </div>
  <div class="brand abs">
    <div class="mark">T&amp;L</div>
    <div class="brand-name">Tembo &amp; Lusani<br>Advocates</div>
  </div>
  <div class="brand-tag">CONSTRUCTION LAW | ARBITRATION | LITIGATION</div>
  <div class="btn-appt abs">Get Appointment</div>
</header>

<section class="hero">
  <div class="photo" role="img" aria-label="Scales of justice on a wooden desk in a warm-lit library"></div>
  <nav class="nav">
    <a>HOME</a><a>ABOUT US</a><a>PRACTICE AREAS</a><a>OUR CLIENTS</a><a>OUR PROFESSIONAL</a><a>CONTACT US</a>
  </nav>
  <div class="hero-title abs">LAW FIRM IN UGANDA</div>
  <div class="hero-sub abs">focusing on Commercial litigation , Construction law and Arbitration</div>
  <div class="arrows abs">
    <span><svg width="10" height="12" viewBox="0 0 10 12"><path d="M8 1L2 6l6 5" fill="none" stroke="#fff" stroke-width="2"/></svg></span>
    <span><svg width="10" height="12" viewBox="0 0 10 12"><path d="M2 1l6 5-6 5" fill="none" stroke="#fff" stroke-width="2"/></svg></span>
  </div>
</section>

<section class="welcome">
  <h1 class="title">Welcome to our website</h1>
  <p>In 1996, our firm was founded and is comprised of 5 Partners and over 15 Associates and support staff fully engaged and focused on client service. The firm is fully automated and is run on the latest practice management software with efficient client focused delivery systems and improved turn around times.<br>Over the years, the firm has worked with the International firm of Harrow Vance in successfully representing Civitas International against a multimillion dollar law suit and has acted for both local and international corporations from China, Italy, Turkey, South Africa, Zambia and the United Kingdom to build their businesses.</p>
  <span class="more">READ MORE ABOUT US</span>
</section>

<section class="about">
  <div class="grey abs"></div>
  <div class="photo statue" role="img" aria-label="Bronze statue of Lady Justice holding scales and a sword"></div>
  <div class="copy abs">
    <div class="label">Who we are</div>
    <h2 class="title" style="margin-top:10px">Using Our Reputation<br>To Help You</h2>
    <p>Tembo &amp; Lusani Advocates are a specialist commercial law firm in Uganda focusing on commercial litigation, construction law and arbitration. We have excelled in our niche areas for over two decades and we continue to grow and be the firm choice in those practice areas.</p>
  </div>
  <div class="photo team" role="img" aria-label="Group photo of the firm's partners and associates in a library"></div>
  <div class="exp abs">
    <div class="small-mark">T&amp;L</div>
    <div class="big">22 YEARS</div>
    <div class="sub">OF EXPERIENCE</div>
    <div class="line"></div>
    <p>5 Partners and over 15 Associates</p>
    <div class="btn">REQUEST A FREE CONSULTATION</div>
  </div>
  <div class="vm abs">
    <h4>VISION</h4>
    <p>To be the firm of choice in our niche practice areas of commercial law</p>
    <h4>MISSION</h4>
    <p>To provide legal services focused on commercial litigation, construction law and arbitration with efficiency, integrity and client satisfaction</p>
  </div>
</section>

<section class="practice">
  <div class="label">Practice areas</div>
  <h2 class="title">We are expert in following areas</h2>
  <div class="card" style="left:95px">
    <div class="icon"><svg width="48" height="48" viewBox="0 0 48 48"><g fill="#fff"><rect x="12" y="8" width="22" height="10" rx="2" transform="rotate(-30 23 13)"/><rect x="22" y="16" width="5" height="22" transform="rotate(-30 24 27)"/><rect x="8" y="40" width="26" height="4"/></g></svg></div>
    <h3>CONSTRUCTION LAW</h3>
    <p>Our Construction Law department is headed by our Senior Partner Daniel Tembo, who is highly qualified and experienced in Construction law and in providing advice on contract management under the standard international forms of contracts.</p>
    <span class="more">READ MORE</span>
  </div>
  <div class="card" style="left:440px">
    <div class="icon"><svg width="48" height="48" viewBox="0 0 48 48"><g fill="#fff"><rect x="12" y="8" width="22" height="10" rx="2" transform="rotate(-30 23 13)"/><rect x="22" y="16" width="5" height="22" transform="rotate(-30 24 27)"/><rect x="8" y="40" width="26" height="4"/></g></svg></div>
    <h3>COMMERCIAL LITIGATION</h3>
    <p>We have a reputation for producing excellent results for our litigation clients. Since 1996, the firm has an excellent track record in winning for our clients in commercial disputes.</p>
    <span class="more">READ MORE</span>
  </div>
  <div class="card" style="left:785px">
    <div class="icon"><svg width="48" height="48" viewBox="0 0 48 48"><g fill="#fff"><rect x="12" y="8" width="22" height="10" rx="2" transform="rotate(-30 23 13)"/><rect x="22" y="16" width="5" height="22" transform="rotate(-30 24 27)"/><rect x="8" y="40" width="26" height="4"/></g></svg></div>
    <h3>ARBITRATION</h3>
    <p>We advise clients on both domestic and international arbitration proceedings and other forms of intermediate and alternative dispute resolution, as well as on contract management of claims arising during the course of a project</p>
    <span class="more">READ MORE</span>
  </div>
</section>

<section class="stats">
  <div class="stat">
    <svg width="48" height="44" viewBox="0 0 48 44" fill="none" stroke="#222" stroke-width="2"><circle cx="24" cy="8" r="5"/><path d="M16 24a8 8 0 0116 0"/><circle cx="10" cy="26" r="4"/><circle cx="38" cy="26" r="4"/><path d="M3 40a7 7 0 0114 0M31 40a7 7 0 0114 0"/></svg>
    <div class="num">05</div><div class="lbl">PARTNERS</div>
  </div>
  <div class="stat">
    <svg width="54" height="44" viewBox="0 0 54 44" fill="none" stroke="#222" stroke-width="2"><circle cx="27" cy="12" r="6"/><path d="M16 36a11 11 0 0122 0"/><circle cx="10" cy="16" r="4"/><circle cx="44" cy="16" r="4"/><path d="M2 34a8 8 0 0114 0M38 34a8 8 0 0114 0"/></svg>
    <div class="num">20+</div><div class="lbl">PEOPLES</div>
  </div>
  <div class="stat">
    <svg width="44" height="44" viewBox="0 0 44 44" fill="none" stroke="#222" stroke-width="2"><rect x="6" y="4" width="32" height="26"/><path d="M12 12h20M12 18h14"/><circle cx="22" cy="34" r="5"/><path d="M18 38l-2 5 6-2 6 2-2-5"/></svg>
    <div class="num">55</div><div class="lbl">YEARS OF COMBINED<br>EXPERIENCE</div>
  </div>
  <div class="stat">
    <svg width="52" height="44" viewBox="0 0 52 44" fill="none" stroke="#222" stroke-width="2"><path d="M2 18l10-8 10 4 8-4 10 2 10 8"/><path d="M12 10l-8 14M42 12l8 14"/><path d="M14 26l6 6 4-2 4 4 6-4 6-6"/></svg>
    <div class="num">350</div><div class="lbl">CASES SOLVED</div>
  </div>
</section>

<section class="team-band">
  <div class="team-nav" style="left:85px"><svg width="8" height="10" viewBox="0 0 8 10"><path d="M6 1L2 5l4 4" fill="none" stroke="#fff" stroke-width="1.5"/></svg></div>
  <div class="member" style="left:110px">
    <div class="photo" role="img" aria-label="Portrait of the managing partner"></div>
    <h4>JOSEPH. K. TEMBO</h4><p>Managing Partner</p>
  </div>
  <div class="member" style="left:365px">
    <div class="photo" role="img" aria-label="Portrait of the senior partner"></div>
    <h4>DANIEL. S. LUSANI</h4><p>Senior Partner</p>
  </div>
  <div class="member" style="left:620px">
    <div class="photo" role="img" aria-label="Portrait of the head of litigation"></div>
    <h4>PAUL MIREMBE</h4><p>Head of Litigation</p>
  </div>
  <div class="team-nav" style="left:822px"><svg width="8" height="10" viewBox="0 0 8 10"><path d="M2 1l4 4-4 4" fill="none" stroke="#fff" stroke-width="1.5"/></svg></div>
  <div class="team-copy">
    <div class="label">Our professionals</div>
    <div class="title">5 Partners &amp;<br>over 15 Associates</div>
    <span class="more">VIEW ALL</span>
  </div>
</section>

<section class="clients">
  <div class="label">Our clients</div>
  <h2 class="title">Commercial Litigation ,Construction &amp; Arbitration clients</h2>
  <div class="c-arrows">
    <span><svg width="8" height="10" viewBox="0 0 8 10"><path d="M6 1L2 5l4 4" fill="none" stroke="#fff" stroke-width="1.5"/></svg></span>
    <span><svg width="8" height="10" viewBox="0 0 8 10"><path d="M2 1l4 4-4 4" fill="none" stroke="#fff" stroke-width="1.5"/></svg></span>
  </div>
  <div class="client" style="left:95px"><i></i>Northline Logistics</div>
  <div class="client" style="left:375px"><i></i>Vantro Surface</div>
  <div class="client" style="left:615px"><i></i>Meridian Media</div>
  <div class="client" style="left:880px"><i></i>Ravine Foods</div>
</section>

<section class="quote">
  <div class="photo" role="img" aria-label="Lawyer reviewing documents at a desk beside a gavel"></div>
  <div class="form">
    <div class="label">Get a free quote</div>
    <h2>Request a free Legal Consultation</h2>
    <p>Whatever your legal concern is, we will be glad to help you solve it. Request an appointment to get started</p>
    <div class="field">Enter your name</div>
    <div class="row"><div class="field">Enter email</div><div class="field">Enter phone no</div></div>
    <div class="field msg">Message</div>
    <div class="submit">Submit</div>
  </div>
</section>

<footer class="footer">
  <div class="addr">
    <h5>HEAD OFFICE ADDRESS &amp; CONTACTS</h5>
    <p>Plot 12, Harbour Avenue<br>3rd Floor, Crescent House<br>P. O Box 4410<br>Kampala, Uganda.</p>
  </div>
  <div class="fmark">T&amp;L</div>
  <div class="social">
    <svg width="12" height="12"><circle cx="6" cy="6" r="5" fill="#fff"/></svg>
    <svg width="12" height="12"><circle cx="6" cy="6" r="5" fill="#fff"/></svg>
    <svg width="12" height="12"><circle cx="6" cy="6" r="5" fill="#fff"/></svg>
  </div>
  <div class="links">
    <h5>QUICK LINKS</h5>
    <div class="cols">
      <div>HOME<br>ABOUT US<br>PRACTICE AREAS</div>
      <div>OUR CLIENTS<br>OUR PROFESSIONAL<br>CONTACT US</div>
    </div>
  </div>
</footer>

<div class="copy-bar abs" style="left:0;width:1200px">© 2018 T&amp;L Firm . All Rights Reserved.</div>

</body>
</html>
```